Flyer Design

I need a flyer designed for a new company in Berkshire called 'Gymzo'. It is a personal training business which will operate from a personal / purpose built gym, with the option of training clients in their homes/local parks. I will offer fitness training, advice, nutrition advice. There will also be bootcamps for customers.

Industry/Entity Type

Nutrition

```html
<!DOCTYPE html>
<html lang="en">
<head>
<meta charset="utf-8">
<title>Gymzo Personal Training Flyer</title>
<link rel="stylesheet" href="https://fonts.googleapis.com/css2?family=Roboto+Condensed:ital,wght@0,400;0,700;1,300&family=Quicksand:wght@400;500;700&display=swap">
<style>
  :root {
    --purple-deep: #4a3a9a;
    --purple-mid: #6b5aad;
    --purple-panel: #7b6bb8;
    --purple-ring: #8a62b4;
    --purple-light: #8f7fc4;
    --teal: #1fb3c3;
    --teal-deep: #10a7b6;
    --teal-text: #14a6b5;
    --white: #ffffff;
    --ink: #1d1d1d;
    --grey: #7a7a7a;
  }
  html, body { margin: 0; padding: 0; overflow: hidden; background: #ffffff; }
  .flyer {
    position: relative; width: 846px; height: 1200px; overflow: hidden;
    font-family: "Quicksand", sans-serif; color: var(--ink);
  }
  .backdrop { position: absolute; inset: 0; }
  .block { position: absolute; margin: 0; }
  .condensed { font-family: "Roboto Condensed", sans-serif; font-weight: 700; }

  .brand { left: 95px; top: 70px; width: 230px; display: flex; align-items: center; justify-content: center; gap: 12px; }
  .brand-dot { width: 22px; height: 22px; border-radius: 50%; background: var(--purple-mid); }
  .brand-name { font-family: "Quicksand", sans-serif; font-weight: 700; font-size: 50px; color: var(--purple-mid); line-height: 1; }

  .title { left: 20px; width: 390px; text-align: center; line-height: 1; }
  .title-top { top: 190px; font-size: 88px; color: var(--purple-deep); }
  .title-bottom { top: 272px; font-size: 72px; color: var(--purple-light); }

  .price { left: 85px; width: 230px; text-align: center; line-height: 1; }
  .price-amount { top: 408px; font-size: 66px; color: var(--purple-deep); }
  .price-unit { top: 487px; font-size: 24px; color: var(--purple-light); }
  .price-note { top: 519px; font-size: 21px; color: var(--grey); font-weight: 400; line-height: 1.1; }
  .price-contact { top: 583px; font-size: 12px; color: var(--ink); line-height: 1.35; }

  .packages-title { left: 72px; top: 682px; font-size: 19px; color: var(--white); }
  .packages { left: 72px; top: 716px; width: 270px; padding: 0; list-style: none; color: var(--white); font-size: 17px; line-height: 25px; }
  .packages li { position: relative; padding-left: 16px; margin-bottom: 12px; }
  .packages li::before { content: ""; position: absolute; left: 2px; top: 11px; width: 4px; height: 4px; background: var(--white); }

  .hello { left: 450px; width: 336px; top: 80px; text-align: center; font-size: 50px; color: var(--white); line-height: 1; }
  .intro { left: 470px; width: 296px; top: 142px; text-align: center; color: var(--white); font-size: 15.5px; line-height: 23px; font-weight: 500; }

  .who { left: 410px; width: 400px; top: 398px; text-align: center; font-size: 47px; color: var(--teal-text); line-height: 1; }
  .who-lead { left: 425px; width: 370px; top: 460px; text-align: center; font-weight: 700; font-size: 16px; line-height: 24px; }
  .who-body { left: 425px; width: 370px; top: 530px; text-align: center; font-size: 16.5px; line-height: 26px; font-weight: 500; }

  .contact-title { left: 440px; width: 350px; top: 872px; text-align: center; font-size: 50px; color: var(--teal-text); line-height: 1; }
  .contact-details { left: 420px; width: 390px; top: 937px; text-align: center; font-size: 16.5px; line-height: 25px; font-weight: 500; }
  .contact-details strong { font-weight: 700; }
  .tagline { left: 410px; width: 410px; top: 1062px; text-align: center; font-family: "Roboto Condensed", sans-serif; font-style: italic; font-weight: 300; font-size: 28px; line-height: 36px; color: var(--purple-mid); }
</style>
</head>
<body>
<main class="flyer">
  <svg class="backdrop" width="846" height="1200" viewBox="0 0 846 1200" xmlns="http://www.w3.org/2000/svg">
    <defs>
      <linearGradient id="tealFrame" x1="0" y1="0" x2="0" y2="1">
        <stop offset="0" stop-color="#16afc0"/>
        <stop offset="1" stop-color="#3cc3cf"/>
      </linearGradient>
      <linearGradient id="purplePanel" x1="0" y1="0" x2="0" y2="1">
        <stop offset="0" stop-color="#7a6ab8"/>
        <stop offset="1" stop-color="#7565b2"/>
      </linearGradient>
      <linearGradient id="portraitTone" x1="0" y1="0" x2="1" y2="1">
        <stop offset="0" stop-color="#9fb7a6"/>
        <stop offset="1" stop-color="#6e6a5a"/>
      </linearGradient>
    </defs>
    <rect width="846" height="1200" fill="#ffffff"/>
    <rect x="420" y="0" width="426" height="1200" fill="url(#tealFrame)"/>
    <rect x="430" y="45" width="375" height="288" fill="var(--teal-deep)"/>
    <rect x="372" y="333" width="433" height="867" fill="#ffffff"/>
    <circle cx="665" cy="1135" r="345" fill="#ffffff" stroke="var(--teal)" stroke-width="12"/>
    <rect x="0" y="0" width="420" height="1200" fill="#5e4ea0"/>
    <rect x="40" y="0" width="332" height="1142" fill="url(#purplePanel)"/>
    <rect x="372" y="333" width="48" height="867" fill="#ffffff"/>
    <circle cx="200" cy="140" r="285" fill="#ffffff" stroke="#5a3f9e" stroke-width="10"/>
    <circle cx="200" cy="510" r="120" fill="#ffffff" stroke="var(--purple-ring)" stroke-width="10"/>
    <circle cx="583" cy="752" r="60" fill="url(#portraitTone)" stroke="var(--teal)" stroke-width="8" role="img" aria-label="Portrait photo of the trainer outdoors"/>
  </svg>

  <div class="block brand" aria-label="Gymzo">
    <span class="brand-dot"></span>
    <span class="brand-name">Gymzo</span>
  </div>

  <h1 class="block title title-top condensed">PERSONAL</h1>
  <p class="block title title-bottom condensed">TRAINING</p>

  <p class="block price price-amount condensed">£40</p>
  <p class="block price price-unit condensed">PER WEEKLY SESSION</p>
  <p class="block price price-note">Discounts for<br>monthly bookings</p>
  <p class="block price price-contact">Contact me for more<br>details</p>

  <h2 class="block packages-title condensed">ALL PACKAGES INCLUDE:</h2>
  <ul class="block packages">
    <li>A one hour free consultation and health discussion</li>
    <li>Body composition analysis</li>
    <li>Food diary and nutritional analysis</li>
    <li>Phone and email support throughout your programme</li>
    <li>Monthly check ups related to goals</li>
    <li>Access to help and tips for nutrition and exercise on members only web link</li>
  </ul>

  <h2 class="block hello condensed">HELLO!</h2>
  <p class="block intro">I'm Laura Hayes and as a qualified personal trainer, I'm here to help you take control of your fitness. Whether you are new to training or just need a new direction, I will work with you to fit a programme to you, your lifestyle and your goals.</p>

  <h2 class="block who condensed">WHO DO I TRAIN?</h2>
  <p class="block who-lead">Gymzo training is tailored to every individual and adapted to their needs.</p>
  <p class="block who-body">So if you are in need of a little bit of motivation, a major lifestyle change or a much needed confidence boost, get in touch!</p>

  <h2 class="block contact-title condensed">CONTACT</h2>
  <p class="block contact-details"><strong>Laura Hayes</strong><br>Email: <strong>laurahayes.train@mailbox.co.uk</strong><br>Tel: <strong>07700 900417</strong></p>

  <p class="block tagline">“Make training a way of life<br>you can always rely on”</p>
</main>
</body>
</html>
```